Business Cards for Internet Security Company

Awesome designers! This is the opportunity to help design cards for a forward thinking network security company. They use threat information gathered from peer groups to make intelligent decisions on what threats are relevant and which arent. ( not that you need this to do designs, but just so you know where they are coming from. ) :-)

We'd like to see a two side design and the deliverables will be in illustrator 4. The logo is attached and the logo colors are attached in the JPG and I've attached a an eps of the logo and icon

Security

```html
<!DOCTYPE html>
<html lang="en">
<head>
<meta charset="utf-8">
<title>Nexward Business Card</title>
<link rel="stylesheet" href="https://fonts.googleapis.com/css2?family=Exo+2:wght@400;600;700&display=swap">
<style>
  :root {
    --brand-blue: #165a96;
    --accent-blue: #3aa6e0;
    --accent-mid: #1f7cc4;
    --card-white: #ffffff;
    --card-grey: #e8e9eb;
    --stage: #d9d6d1;
    --text-light: #ffffff;
  }
  * { margin: 0; padding: 0; box-sizing: border-box; }
  html, body {
    width: 1200px; height: 433px; overflow: hidden;
    background: var(--stage);
    font-family: "Exo 2", sans-serif;
  }
  .sheet {
    width: 1200px; height: 433px;
    display: flex; align-items: center; justify-content: space-around;
    padding: 0 40px;
  }
  .card {
    position: relative;
    width: 500px; height: 286px;
    overflow: hidden;
    box-shadow: 0 8px 20px rgba(0,0,0,0.25);
  }
  .card-front { background: var(--brand-blue); }
  .front-panel { position: absolute; inset: 0; }
  .brand-lockup {
    position: absolute; left: 34px; top: 120px;
    display: flex; align-items: center; gap: 10px;
    color: var(--brand-blue);
  }
  .brand-dot {
    width: 26px; height: 26px; border-radius: 50%;
    background: var(--accent-blue);
  }
  .brand-name { font-size: 30px; font-weight: 600; letter-spacing: 0.5px; }
  .contact-block {
    position: absolute; right: 28px; top: 30px;
    text-align: right; color: var(--text-light);
  }
  .person-name { font-size: 18px; font-weight: 700; letter-spacing: 1px; }
  .person-title { font-size: 12.5px; line-height: 1.35; margin-top: 2px; }
  .address { font-size: 12.5px; line-height: 1.4; margin-top: 22px; }
  .contact-list { list-style: none; margin-top: 20px; font-size: 12px; }
  .contact-list li {
    display: flex; justify-content: flex-end; align-items: center;
    gap: 8px; line-height: 1.9;
  }
  .contact-list svg { width: 12px; height: 12px; fill: var(--text-light); }
  .card-back { background: var(--card-grey); }
  .back-name {
    position: absolute; right: 34px; top: 58px;
    font-size: 38px; font-weight: 600; color: var(--brand-blue);
  }
  .back-mark {
    position: absolute; left: 60px; bottom: 44px;
    width: 110px; height: 110px; border-radius: 50%;
    background: var(--brand-blue);
  }
</style>
</head>
<body>
<main class="sheet">
  <section class="card card-front" aria-label="Card front">
    <svg class="front-panel" viewBox="0 0 500 286" preserveAspectRatio="none" aria-hidden="true">
      <path d="M0,0 H214 Q262,140 196,286 H0 Z" fill="var(--accent-blue)"/>
      <path d="M0,0 H204 Q250,140 186,286 H0 Z" fill="var(--accent-mid)"/>
      <path d="M0,0 H196 Q240,140 178,286 H0 Z" fill="var(--card-white)"/>
    </svg>
    <div class="brand-lockup">
      <span class="brand-dot"></span>
      <span class="brand-name">Nexward</span>
    </div>
    <div class="contact-block">
      <p class="person-name">DAN MORROW</p>
      <p class="person-title">Chief Executive Officer<br>&amp; Co-Founder</p>
      <p class="address">12, 4th floor Plaza<br>Harbour Lane QTR</p>
      <ul class="contact-list">
        <li>012 555 0147
          <svg viewBox="0 0 12 12"><path d="M2 1h2.5l1 3-1.5 1a7 7 0 0 0 3 3l1-1.5 3 1V11C5 11 1 7 1 2z"/></svg></li>
        <li>012 555 0148
          <svg viewBox="0 0 12 12"><path d="M3 0h6v12H3zM4 1v9h4V1z"/></svg></li>
        <li>dan@nexward.example
          <svg viewBox="0 0 12 12"><path d="M0 2h12v8H0zM1 3l5 4 5-4v-.2H1z"/></svg></li>
        <li>www.nexward.example
          <svg viewBox="0 0 12 12"><circle cx="6" cy="6" r="5.5"/></svg></li>
      </ul>
    </div>
  </section>

  <section class="card card-back" aria-label="Card back">
    <span class="back-mark"></span>
    <p class="back-name">Nexward</p>
  </section>
</main>
</body>
</html>
```